Emergency Medical Training and Events Company Business Needs Business Card Design

We are in need of a business card for our dynamic company expanding its customer base and need to be easily contacted and identified for when we visit with government officials, potential EMS / Fire agencies and county coordinators to arrange for training programs for first responders to better prepare them for critical thinking at critical incidents.

Target Market(s)

EMS/Fire and Event Promoters

Industry/Entity Type

Medical

Contact Information for Business Card

Two cards, comparable designs:

Martin K. Halvey, Principal, m.halvey@rvqtlo.com
Owen Tash, Event and Training Specialist, o.tash@rvqtlo.com

Font styles to use
Other font styles liked:
• Cambria

Colors

Designer to choose colors to be used in the design.

Requirements
Must have
• Company Logo, Spots for Name, Title, Phone Number, Email, Website
• A bullet list stating that we offer, QRB CPR and First Aid Instructors, Hold the Line Instructors, Event EMS, CME's, MCI Training and Planning. We prefer to have a black background for the card but if you can make a blue or white card stand out we would review that as well.
Should not have
• Tacky logos or special sayings ... simple, elegant, professional is the look we seek

```html
<!DOCTYPE html>
<html lang="en">
<head>
<meta charset="utf-8">
<title>RVQ Training Lodge – Business Card</title>
<link href="https://fonts.googleapis.com/css2?family=Montserrat:wght@400;500;600;700&display=swap" rel="stylesheet">
<style>
  :root {
    --navy: #1a1d4e;
    --red: #c42026;
    --white: #ffffff;
    --ink: #2b2b3a;
    --muted: #55586a;
    --backdrop: #ecebe8;
  }
  * { margin: 0; padding: 0; box-sizing: border-box; }
  html, body {
    width: 1200px; height: 900px; overflow: hidden;
    background: var(--backdrop);
    font-family: "Montserrat", Arial, sans-serif;
  }
  .canvas { position: relative; width: 1200px; height: 900px; }
  .card {
    position: absolute; left: 311px; width: 577px; height: 329px;
    overflow: hidden;
  }
  /* Front card */
  .card-front { top: 98px; background: var(--navy); }
  .front-brand {
    position: absolute; left: 0; top: 0; width: 100%; height: 270px;
    display: flex; align-items: center; justify-content: center;
    color: var(--white); font-weight: 700; font-size: 34px;
    letter-spacing: 1px; text-transform: uppercase;
  }
  .services {
    position: absolute; left: 0; bottom: 0; width: 100%; height: 59px;
    background: var(--red); color: var(--white);
    font-size: 14.5px; font-weight: 500; line-height: 20px;
    text-align: center; padding-top: 9px;
  }
  /* Back card */
  .card-back { top: 472px; background: var(--white); }
  .brand {
    position: absolute; left: 34px; top: 126px; width: 260px;
    display: flex; align-items: center; gap: 12px;
  }
  .brand-dot {
    width: 56px; height: 56px; border-radius: 50%;
    background: var(--red); flex-shrink: 0;
  }
  .brand-name {
    color: var(--navy); font-weight: 700; font-size: 21px;
    line-height: 24px; text-transform: uppercase;
  }
  .divider {
    position: absolute; left: 309px; top: 106px;
    width: 2px; height: 115px; background: var(--navy);
  }
  .person { position: absolute; left: 334px; top: 102px; }
  .person-name {
    color: var(--navy); font-weight: 700; font-size: 17px;
    letter-spacing: 0.5px; text-transform: uppercase;
  }
  .person-title { color: var(--muted); font-size: 13px; margin-top: 1px; }
  .contacts { list-style: none; margin-top: 16px; }
  .contacts li {
    display: flex; align-items: center; gap: 10px;
    color: var(--ink); font-size: 15px; height: 24px;
  }
  .contacts svg { width: 15px; height: 15px; fill: var(--navy); }
  .wave { position: absolute; left: 0; top: 0; width: 577px; height: 329px; }
  .website {
    position: absolute; left: 46px; top: 289px;
    color: var(--white); font-size: 14px; font-weight: 500;
  }
</style>
</head>
<body>
<main class="canvas">
  <section class="card card-front">
    <div class="front-brand">RVQ Training Lodge</div>
    <div class="services">
      QRB CPR and First Aid Instructors • Hold the Line Instructors<br>
      Event EMS • CME's • MCI Training and Planning
    </div>
  </section>

  <section class="card card-back">
    <svg class="wave" viewBox="0 0 577 329" aria-hidden="true">
      <path fill="var(--navy)" d="M270,282 C380,305 480,300 577,262 L577,290 C490,318 390,314 270,282Z"/>
      <path fill="var(--red)" d="M0,282 C110,262 250,270 350,298 C440,322 520,312 577,290 L577,329 L0,329Z"/>
    </svg>
    <div class="brand">
      <span class="brand-dot"></span>
      <span class="brand-name">RVQ Training Lodge</span>
    </div>
    <div class="divider"></div>
    <div class="person">
      <p class="person-name">Owen Tash</p>
      <p class="person-title">Partner</p>
      <ul class="contacts">
        <li>
          <svg viewBox="0 0 24 24"><path d="M6.6 10.8a15.2 15.2 0 0 0 6.6 6.6l2.2-2.2a1 1 0 0 1 1-.25 11.4 11.4 0 0 0 3.6.57 1 1 0 0 1 1 1V20a1 1 0 0 1-1 1A17 17 0 0 1 3 4a1 1 0 0 1 1-1h3.5a1 1 0 0 1 1 1c0 1.25.2 2.45.57 3.57a1 1 0 0 1-.25 1z"/></svg>
          123 456 7890
        </li>
        <li>
          <svg viewBox="0 0 24 24"><path d="M7 1h10a2 2 0 0 1 2 2v18a2 2 0 0 1-2 2H7a2 2 0 0 1-2-2V3a2 2 0 0 1 2-2zm0 3v14h10V4zm5 15.5a1 1 0 1 0 0 2 1 1 0 0 0 0-2z"/></svg>
          555 014 2287
        </li>
        <li>
          <svg viewBox="0 0 24 24"><path d="M2 5h20v14H2zm2 2v.4l8 5 8-5V7zm0 2.8V17h16V9.8l-8 5z"/></svg>
          o.tash@rvqtlo.com
        </li>
      </ul>
    </div>
    <p class="website">www.rvqtlo.com</p>
  </section>
</main>
</body>
</html>
```